Wheels Open Doors - Two sided invitation to encourage bike friendly businesses

Pedal Haven is a charitable trust who want to grow everyday bike use. One way to do that is help businesses understand that 'Wheels Open Doors'. We want a postcard sized 'invitation' that bike users can give to their favourite businesses, inviting them to find out more about all the benefits of attracting bike users to their business and becoming a 'Pedal Haven Business'. We are currently finalising copy, so the attached is indicative but not final copy. The docx file is the words, the png is indicative of the type of infographic we might want to feature.
I'm also attaching a mock up of our window sticker for businesses, and some social shares featuring photographic images which we have available to use. This will give you an idea of our branding to date. Our extended branding concept (which we will use when we re-do our website) is based on icons, so I'm open to seeing icon focused designs also.
The feel needs to be inviting, credible, enticing, business like, noticeable, with a strong call to action.

Target Market(s)

Small business operators: retail, cafes, etc; also managers of larger chains such as supermarkets, gyms, etc.

Industry/Entity Type

Non Profit

Font styles to use
Serif
Other font styles liked:
• Logo is done in Raleway, so need compatible font.

Colors
9ccb3b

Requirements
Must have
• Two Sides
• Use the copy provided
• Strong call to action - visiting website
• Use our colours
• A6 sized cards
Nice to have
• Compelling images and/or infographic
• Consistency with circles / curves used in other branding.
Should not have
• Not bland, not something that will get lost on the recipients desk or counter.

```html
<!DOCTYPE html>
<html lang="en">
<head>
<meta charset="utf-8">
<title>Pedal Haven – Invitation Card</title>
<link rel="stylesheet" href="https://fonts.googleapis.com/css2?family=Raleway:wght@400;500;700&family=Yellowtail&display=swap">
<style>
  :root {
    --green: #44b649;
    --green-dark: #2f9a3c;
    --ink: #666666;
    --panel: #f4f4f4;
    --page: #ffffff;
    --white: #ffffff;
    --heart: #d9343a;
  }
  * { box-sizing: border-box; margin: 0; padding: 0; }
  html, body { width: 1000px; height: 1200px; overflow: hidden; background: var(--page); }
  body { font-family: "Raleway", Arial, sans-serif; position: relative; }

  .card {
    position: absolute; left: 115px; top: 55px; width: 770px; height: 1090px;
    background: var(--panel);
    box-shadow: 0 4px 18px rgba(0,0,0,0.18);
    overflow: hidden;
  }
  .hero {
    position: absolute; left: 0; top: 0; width: 770px; height: 545px; overflow: hidden;
    background:
      radial-gradient(ellipse at 75% 35%, #f1e2c8 0%, rgba(241,226,200,0) 55%),
      radial-gradient(ellipse at 15% 30%, #3f6b2c 0%, rgba(63,107,44,0) 60%),
      linear-gradient(100deg, #4b6a34 0%, #8c7a5c 40%, #d9c2a0 70%, #efe3cf 100%);
  }
  .hero-mark { position: absolute; left: 36px; top: 32px; display: flex; align-items: center; gap: 14px; }
  .hero-mark .disc { width: 134px; height: 134px; border-radius: 50%; background: var(--white); border: 6px solid #d8d8d8; }
  .hero-mark .name { font-size: 31px; font-weight: 500; line-height: 32px; color: var(--white); width: 150px; }
  .hero-question {
    position: absolute; left: 37px; top: 176px; width: 142px;
    font-size: 19px; line-height: 24px; color: var(--white);
  }
  .hashtag {
    position: absolute; right: 40px; top: 445px;
    display: flex; align-items: center; gap: 8px; white-space: nowrap;
  }
  .hashtag .hash {
    width: 58px; height: 58px; border-radius: 50%; background: var(--green);
    color: var(--white); font: 700 34px/58px "Raleway", sans-serif; text-align: center;
  }
  .hashtag .tag { font-family: "Yellowtail", cursive; font-size: 58px; line-height: 60px; color: var(--white); }

  .brand { position: absolute; left: 48px; top: 572px; display: flex; align-items: center; gap: 10px; }
  .brand .disc { width: 98px; height: 98px; border-radius: 50%; background: var(--white); border: 5px solid #d0d0d0; }
  .brand .name { font-size: 21px; font-weight: 500; line-height: 23px; color: var(--green); width: 110px; }

  .benefit-icons { position: absolute; left: 403px; top: 588px; display: flex; gap: 21px; }
  .benefit-icons svg { width: 64px; height: 64px; }

  .why { position: absolute; left: 70px; top: 682px; width: 665px; color: var(--ink); }
  .why h2 { font-size: 23px; font-weight: 700; color: var(--green); line-height: 28px; }
  .benefits { list-style: none; font-size: 17.5px; line-height: 22.5px; }
  .benefits li { position: relative; }
  .benefits li::before {
    content: ""; position: absolute; left: -23px; top: 5px; width: 11px; height: 6px;
    border-left: 3px solid var(--green); border-bottom: 3px solid var(--green);
    transform: rotate(-45deg);
  }
  .heart { color: var(--heart); font-size: 20px; padding: 0 4px; }
  .study { margin-top: 12px; width: 600px; font-size: 17.5px; line-height: 22.5px; }
  .hl { color: var(--green); }

  .think { position: absolute; left: 70px; top: 912px; color: var(--ink); font-size: 17.5px; line-height: 22px; }
  .think h3, .cta h3 { font-size: 24px; font-weight: 700; color: var(--green); line-height: 28px; }
  .cta { position: absolute; left: 70px; top: 994px; color: var(--ink); font-size: 17.5px; line-height: 22px; }

  .social { position: absolute; left: 523px; top: 977px; list-style: none; font-size: 17.5px; line-height: 22px; color: var(--ink); }
  .social li { display: flex; align-items: center; gap: 3px; }
  .social .dot { width: 15px; height: 15px; border-radius: 50%; background: var(--ink); display: inline-block; }
</style>
</head>
<body>
<main class="card">
  <section class="hero" role="img" aria-label="Photograph of a smiling couple in sun hats riding bicycles down a leafy street, a basket of flowers on the front bike">
    <div class="hero-mark">
      <span class="disc"></span>
      <span class="name">Pedal Haven</span>
    </div>
    <p class="hero-question">Why make biking customers - and their $$$ - welcome at your business?</p>
    <div class="hashtag">
      <span class="hash">#</span>
      <span class="tag">pedalon</span>
    </div>
  </section>

  <div class="brand">
    <span class="disc"></span>
    <span class="name">Pedal Haven</span>
  </div>

  <div class="benefit-icons">
    <svg viewBox="0 0 64 64" aria-label="Spending">
      <circle cx="32" cy="32" r="32" fill="var(--green)"/>
      <circle cx="32" cy="32" r="17" fill="none" stroke="#fff" stroke-width="5" stroke-dasharray="80 8"/>
      <text x="32" y="38" text-anchor="middle" font-family="Raleway, sans-serif" font-weight="700" font-size="17" fill="#fff">$</text>
    </svg>
    <svg viewBox="0 0 64 64" aria-label="Bike parking">
      <circle cx="32" cy="32" r="32" fill="var(--green)"/>
      <rect x="16" y="16" width="32" height="32" rx="4" fill="none" stroke="#fff" stroke-width="3"/>
      <text x="26" y="38" text-anchor="middle" font-family="Raleway, sans-serif" font-weight="700" font-size="18" fill="#fff">P</text>
      <circle cx="35" cy="41" r="3" fill="none" stroke="#fff" stroke-width="1.5"/>
      <circle cx="43" cy="41" r="3" fill="none" stroke="#fff" stroke-width="1.5"/>
      <path d="M35 41 L38 36 L43 41 M38 36 L41 36" fill="none" stroke="#fff" stroke-width="1.5"/>
    </svg>
    <svg viewBox="0 0 64 64" aria-label="Cafe">
      <circle cx="32" cy="32" r="32" fill="var(--green)"/>
      <path d="M18 32 H42 V36 C42 44 36 47 30 47 C24 47 18 44 18 36 Z" fill="#fff"/>
      <path d="M42 34 C49 34 49 42 41 42" fill="none" stroke="#fff" stroke-width="3"/>
      <path d="M14 49 H46" stroke="#fff" stroke-width="3" stroke-linecap="round"/>
      <path d="M25 28 C22 24 28 22 25 17 M31 28 C28 24 34 22 31 17" fill="none" stroke="#fff" stroke-width="2.5" stroke-linecap="round"/>
    </svg>
    <svg viewBox="0 0 64 64" aria-label="Bicycle">
      <circle cx="32" cy="32" r="32" fill="var(--green)"/>
      <circle cx="20" cy="38" r="8" fill="none" stroke="#fff" stroke-width="2.5"/>
      <circle cx="44" cy="38" r="8" fill="none" stroke="#fff" stroke-width="2.5"/>
      <path d="M20 38 L27 26 L40 26 L44 38 M27 26 L32 38 L40 26 M24 22 H30 M38 22 L40 26" fill="none" stroke="#fff" stroke-width="2.5" stroke-linejoin="round"/>
    </svg>
  </div>

  <section class="why">
    <h2>Why welcome bikes?</h2>
    <ul class="benefits">
      <li>Biking customers spend $$$ where parking’s easy.</li>
      <li>They spend $$$ locally as they must carry what they buy.</li>
      <li>Biking customers move slower, so see what your business offers.</li>
      <li>They tell friends where’s good to park and shop, where they feel welcome.</li>
      <li>You’re helping people be environmentally, budget and heart friendly – and<br>they’ll <span class="heart">♡</span> you for it.</li>
    </ul>
    <p class="study">A Melbourne study showed swapping a car park for six bike parks<br>could increase the space’s retail spend from <span class="hl">$27</span> to <span class="hl">$97.20</span> an hour.</p>
  </section>

  <section class="think">
    <h3>Just think</h3>
    <p><span class="hl">every bike</span> parked by someone else’s<br>business <span class="hl">could have been your customer.</span></p>
  </section>

  <section class="cta">
    <h3>pedalhaven.org</h3>
    <p>to see how you can become<br>a pedal haven business.</p>
  </section>

  <ul class="social">
    <li><span class="dot"></span>/Pedal Haven</li>
    <li><span class="dot"></span>/@PedalHaven</li>
    <li><span class="dot"></span>/Pedal Haven</li>
    <li><span class="dot"></span>/PedalHaven</li>
  </ul>
</main>
</body>
</html>
```